Apartments rental business needs a web for direct reservations.

I need a website that allows my clients to check the property (pictures, a brief description etc) and lets them make reservations. They will be providing the required information such as name, last name, email address and credit card details. Also a calendar where I can update the availability (dates and prices) of the property upon new reservations is a must. I already have a logo that should also be a good starting point for colors, style an inspiration.

```html
<!DOCTYPE html>
<html lang="en">
<head>
<meta charset="utf-8">
<title>Casa Coral Bungalows</title>
<link href="https://fonts.googleapis.com/css2?family=Montserrat:wght@400;600;700;800&family=Lato:ital,wght@0,400;0,700;1,400&display=swap" rel="stylesheet">
<style>
:root{
  --teal:#34a898;
  --teal-dark:#24907f;
  --orange:#f26a21;
  --orange-red:#e9492a;
  --blue:#27a3dc;
  --ink:#2f2f2f;
  --muted:#5c5c5c;
  --line:#e3e3e3;
  --white:#ffffff;
}
*{box-sizing:border-box;margin:0;padding:0}
html,body{width:1200px;height:4905px;overflow:hidden}
body{position:relative;background:var(--white);font-family:'Lato',sans-serif;color:var(--ink)}
.abs{position:absolute}
h1,h2,h3,h4{font-family:'Montserrat',sans-serif}

/* header */
.site-header{left:0;top:0;width:1200px;height:130px;background:var(--white)}
.brand{left:180px;top:32px;display:flex;align-items:center;gap:10px}
.brand-dot{width:34px;height:34px;border-radius:50%;background:var(--orange)}
.brand-name{font-family:'Montserrat',sans-serif;font-weight:700;font-size:19px;color:var(--teal);letter-spacing:.5px}
.contact{top:20px;display:flex;align-items:center;gap:10px;font-family:'Montserrat',sans-serif;font-size:13px}
.contact .label{color:var(--orange);font-weight:600;display:block}
.contact .value{color:var(--teal);font-weight:600}
.nav{right:173px;top:90px;display:flex;gap:34px;font-family:'Montserrat',sans-serif;font-size:12.5px;font-weight:600;color:var(--ink)}

/* hero */
.hero{left:0;top:130px;width:1200px;height:690px;overflow:hidden}
.hero-photo{position:absolute;inset:0;background:linear-gradient(180deg,#5c7f95 0%,#7fa7b8 20%,#3e6b3a 42%,#8a6a4e 62%,#a57756 78%,#6b5a4c 100%)}
.hero-title{position:absolute;left:0;width:100%;top:255px;text-align:center;color:var(--white);font-family:'Montserrat',sans-serif;font-weight:800;font-size:42px;letter-spacing:1px;text-shadow:0 2px 8px rgba(0,0,0,.45)}
.btn{display:inline-block;background:var(--orange);color:var(--white);font-family:'Montserrat',sans-serif;font-weight:700;font-size:13px;border-radius:4px;text-align:center}
.hero .btn{position:absolute;left:540px;top:330px;width:120px;height:36px;line-height:36px}
.slide-arrow{position:absolute;width:30px;height:30px;border:2px solid rgba(255,255,255,.8);border-radius:50%}
.slide-arrow svg{display:block;margin:7px auto}

/* reservation */
.reservation{left:0;top:780px;width:1200px;height:420px}
.reservation-bg{position:absolute;inset:0}
.res-title{left:173px;top:118px;color:var(--white);font-weight:700;font-size:26px;letter-spacing:.5px}
.res-text{left:173px;top:158px;width:260px;color:#e8fffb;font-size:14px;line-height:18px}
.field{height:40px;border:1.5px solid rgba(255,255,255,.85);border-radius:3px;color:var(--white);font-size:13px;padding:0 12px;line-height:37px;display:flex;justify-content:space-between;align-items:center}
.res-btn{left:925px;top:272px;width:102px;height:32px;line-height:32px}

/* apartment */
.apt-title{left:173px;top:1275px;font-size:25px;font-weight:600;color:var(--ink);letter-spacing:.3px}
.meta{top:1326px;display:flex;align-items:center;gap:10px;font-size:12.5px;color:var(--muted)}
.pin{width:22px;height:22px;border-radius:50%;background:var(--orange);display:flex;align-items:center;justify-content:center}
.gallery-main{left:173px;top:1400px;width:854px;height:448px;background:linear-gradient(90deg,#6d4a3a 0%,#a0745b 30%,#c9b8a8 52%,#8aa36a 70%,#5d7f3f 100%)}
.gallery-arrow{top:1590px}
.thumbs{left:173px;top:1854px;width:854px;height:288px;display:grid;grid-template-columns:repeat(4,1fr);grid-template-rows:1fr 1fr;gap:6px}
.thumb{border-radius:1px}
.thumb.tall{grid-column:4;grid-row:1/3}

.desc{left:173px;top:2190px;width:550px;font-size:13.5px;line-height:21px;color:var(--ink)}
.desc p{margin-bottom:16px}
.popular{left:173px;top:2725px;width:400px}
.popular h4{font-size:15px;font-weight:700;margin-bottom:12px}
.popular li{list-style:none;display:flex;align-items:center;gap:14px;font-size:13px;height:29px}
.popular svg{width:28px;height:22px}
.surroundings{left:772px;top:2190px;width:255px;font-size:12.5px;color:var(--ink)}
.surroundings h4{font-size:15px;font-weight:700;margin-bottom:14px}
.surroundings h5{font-family:'Montserrat',sans-serif;font-size:13.5px;font-weight:600;color:var(--teal);margin:18px 0 8px}
.surroundings li{list-style:none;display:flex;gap:10px;height:24px;align-items:center}
.surroundings li span{color:var(--muted)}

/* facilities */
.facilities{left:0;top:2960px;width:1200px;height:660px}
.fac-title{left:0;width:1200px;top:146px;text-align:center;color:var(--white);font-size:25px;font-weight:700}
.fac-col{top:225px;width:170px;color:var(--white)}
.fac-col svg{width:64px;height:56px;display:block;margin-bottom:14px}
.fac-col h4{font-size:15px;font-weight:700;line-height:18px;margin-bottom:10px}
.fac-col li{font-size:12.5px;line-height:22px;list-style:none;padding-left:12px;position:relative}
.fac-col li::before{content:"";position:absolute;left:0;top:9px;width:4px;height:4px;border-radius:50%;background:var(--white)}

.map{left:0;top:3615px;width:1200px;height:390px;background:linear-gradient(135deg,#ecebe7 0%,#e1e0db 50%,#eceae5 100%)}

/* reviews */
.rev-title{left:0;width:1200px;top:4100px;text-align:center;font-size:26px;font-weight:600;letter-spacing:1.5px}
.rev-text{left:245px;top:4165px;width:710px;text-align:center;font-style:italic;font-size:13.5px;line-height:22px;color:var(--ink)}
.avatar{left:458px;top:4298px;width:116px;height:116px;border-radius:50%;border:5px solid var(--teal);background:radial-gradient(circle at 50% 40%,#b89a85 0%,#6b5a4f 60%,#3c3430 100%)}
.rev-name{left:590px;top:4310px;font-family:'Montserrat',sans-serif;font-weight:700;font-size:30px;color:var(--orange)}
.rev-lang{left:590px;top:4356px;font-style:italic;font-size:14px}

/* footer */
.footer{left:0;top:4420px;width:1200px;height:485px}
.foot-brand{left:173px;top:170px;width:220px;text-align:center}
.foot-dot{width:96px;height:96px;border-radius:50%;background:var(--white);margin:0 auto 16px}
.foot-name{font-family:'Montserrat',sans-serif;font-weight:700;font-size:26px;color:var(--white);letter-spacing:1px}
.foot-col{top:168px;color:var(--white)}
.foot-col h4{font-size:16px;font-weight:700;margin-bottom:12px}
.foot-col li{list-style:none;font-size:12px;line-height:19px;color:#e3fbf7}
.copyright{left:173px;top:445px;font-size:11.5px;color:var(--white)}
.social{left:905px;top:438px;display:flex;gap:8px}
.social span{width:22px;height:22px;border-radius:50%;display:block}
.lang{left:1093px;top:444px;font-size:11px;color:var(--white);font-weight:700}
</style>
</head>
<body>

<header class="site-header abs">
  <div class="brand abs"><span class="brand-dot"></span><span class="brand-name">CASA CORAL</span></div>
  <div class="contact abs" style="left:680px">
    <svg width="30" height="30" viewBox="0 0 24 24"><path fill="var(--teal)" d="M6.6 10.8a15 15 0 0 0 6.6 6.6l2.2-2.2c.3-.3.7-.4 1-.2 1.1.4 2.3.6 3.6.6.6 0 1 .4 1 1V20c0 .6-.4 1-1 1A17 17 0 0 1 3 4c0-.6.4-1 1-1h3.5c.6 0 1 .4 1 1 0 1.3.2 2.5.6 3.6.1.3 0 .7-.2 1z"/></svg>
    <div><span class="label">Call us:</span><span class="value">555 010 2030</span></div>
  </div>
  <div class="contact abs" style="left:845px">
    <svg width="34" height="26" viewBox="0 0 34 26"><rect x="1" y="2" width="32" height="22" rx="2" fill="var(--teal)"/><path d="M2 4l15 11L32 4" stroke="#fff" stroke-width="2" fill="none"/></svg>
    <div><span class="label">Mail us:</span><span class="value">hello@casacoral.example</span></div>
  </div>
  <nav class="nav abs"><span>HOME</span><span>APARTMENT INFO &amp; PRICE</span><span>FACILITIES</span><span>HOUSE RULES</span><span>REVIEWS</span><span>CONTACT</span></nav>
</header>

<section class="hero abs">
  <div class="hero-photo" role="img" aria-label="Sunny pool terrace with loungers, palm trees and bungalows"></div>
  <span class="slide-arrow" style="left:28px;top:268px"><svg width="12" height="12" viewBox="0 0 12 12"><path d="M8 1L3 6l5 5" stroke="#fff" stroke-width="2" fill="none"/></svg></span>
  <span class="slide-arrow" style="right:28px;top:268px"><svg width="12" height="12" viewBox="0 0 12 12"><path d="M4 1l5 5-5 5" stroke="#fff" stroke-width="2" fill="none"/></svg></span>
  <h1 class="hero-title">THE CASA CORAL BUNGALOW</h1>
  <span class="btn">BOOK NOW</span>
</section>

<section class="reservation abs">
  <svg class="reservation-bg" width="1200" height="420" viewBox="0 0 1200 420" preserveAspectRatio="none">
    <defs><linearGradient id="sunset" x1="0" x2="1"><stop offset="0" stop-color="#f6a24a"/><stop offset=".5" stop-color="#f26a21"/><stop offset="1" stop-color="#e9492a"/></linearGradient></defs>
    <path d="M0 20 C250 80 450 -10 700 30 C900 60 1050 10 1200 40 V420 H0Z" fill="#fff"/>
    <path d="M0 34 C250 94 450 4 700 44 C900 74 1050 24 1200 54 V420 H0Z" fill="var(--blue)"/>
    <path d="M0 48 C250 108 450 18 700 58 C900 88 1050 38 1200 68 V420 H0Z" fill="#fff"/>
    <path d="M0 58 C250 118 450 28 700 68 C900 98 1050 48 1200 78 V420 H0Z" fill="var(--teal)"/>
    <path d="M0 300 C200 280 400 390 650 330 C850 285 1000 330 1200 300 V420 H0Z" fill="url(#sunset)"/>
    <path d="M0 340 C220 310 420 410 660 360 C860 320 1020 360 1200 330 V420 H0Z" fill="#fff"/>
  </svg>
  <h2 class="res-title abs">RESERVATION</h2>
  <p class="res-text abs">Sed ut perspiciatis unde omnis iste natus error sit voluptatem accusantium doloremque laudantium, totam rem aperiam, eaque ipsa quae ab</p>
  <div class="field abs" style="left:480px;top:122px;width:275px">Name</div>
  <div class="field abs" style="left:760px;top:122px;width:267px">Last Name</div>
  <div class="field abs" style="left:480px;top:171px;width:275px">Email address</div>
  <div class="field abs" style="left:760px;top:171px;width:185px">Credit Card Number</div>
  <div class="field abs" style="left:950px;top:171px;width:77px">CVV</div>
  <div class="field abs" style="left:480px;top:220px;width:255px">DD/MM<svg width="14" height="14" viewBox="0 0 14 14"><rect x="1" y="2" width="12" height="11" rx="1" stroke="#fff" fill="none" stroke-width="1.5"/><path d="M1 5h12" stroke="#fff" stroke-width="1.5"/></svg></div>
  <div class="field abs" style="left:760px;top:220px;width:267px">Room<svg width="10" height="6" viewBox="0 0 10 6"><path d="M0 0h10L5 6z" fill="#fff"/></svg></div>
  <span class="btn res-btn abs">BOOK NOW</span>
</section>

<h2 class="apt-title abs">APARTMENT CASA CORAL BUNGALOWS</h2>
<div class="meta abs" style="left:173px"><span class="pin"><svg width="10" height="12" viewBox="0 0 10 12"><path d="M5 0a4 4 0 0 1 4 4c0 3-4 8-4 8S1 7 1 4a4 4 0 0 1 4-4z" fill="#fff"/></svg></span>22 Calle del Faro, 35100 Costa Sol, Spain</div>
<div class="meta abs" style="left:857px"><span class="pin"><svg width="12" height="12" viewBox="0 0 12 12"><circle cx="6" cy="4" r="2.5" fill="#fff"/><path d="M1 12a5 5 0 0 1 10 0z" fill="#fff"/></svg></span>Great for two travellers</div>

<div class="gallery-main abs" role="img" aria-label="Bungalow patio with table and chairs beside a garden lawn"></div>
<span class="slide-arrow gallery-arrow abs" style="left:105px;border:none"><svg width="16" height="30" viewBox="0 0 16 30"><path d="M14 1L2 15l12 14" stroke="#bbb" stroke-width="2" fill="none"/></svg></span>
<span class="slide-arrow gallery-arrow abs" style="left:1063px;border:none"><svg width="16" height="30" viewBox="0 0 16 30"><path d="M2 1l12 14L2 29" stroke="#bbb" stroke-width="2" fill="none"/></svg></span>
<div class="thumbs abs">
  <div class="thumb" style="background:linear-gradient(135deg,#d8d4cc,#8c8a84)" role="img" aria-label="Kitchen"></div>
  <div class="thumb" style="background:linear-gradient(135deg,#e9e4dc,#9bb07a)" role="img" aria-label="Bungalow exterior"></div>
  <div class="thumb" style="background:linear-gradient(135deg,#d9e0e6,#7d93a6)" role="img" aria-label="Bedroom"></div>
  <div class="thumb tall" style="background:linear-gradient(160deg,#6f8c55,#c9c1ad 60%,#7a7164)" role="img" aria-label="Sun loungers on the lawn"></div>
  <div class="thumb" style="background:linear-gradient(135deg,#d24b3a,#7fa35a)" role="img" aria-label="Flowering garden"></div>
  <div class="thumb" style="background:linear-gradient(135deg,#b9b3a8,#6e6a63)" role="img" aria-label="Living room"></div>
  <div class="thumb" style="background:linear-gradient(135deg,#6bb6d4,#e8e2d6)" role="img" aria-label="Swimming pool"></div>
</div>

<div class="desc abs">
  <p>Located in Costa Sol, within 4.1 km of the Aqua Park and 6 km of Playa del Sur, Casa Coral Bungalows 45 &amp; 46 offers accommodation with free WiFi, air conditioning, an outdoor swimming pool and a garden. The property has garden views and is 12 km from the Palm Park.</p>
  <p>The apartment features 2 bedrooms, a flat-screen TV with satellite channels, an equipped kitchen with a dishwasher and a microwave, a washing machine, and 1 bathroom with a shower.</p>
  <p>A children's playground is available on site and hiking can be enjoyed within close proximity of the apartment.</p>
  <p>Costa Sol Lighthouse is 3.8 km from Casa Coral Bungalows 45 &amp; 46. The nearest airport is Costa Sol Airport, 31 km from the accommodation.</p>
  <p>This is our guests' favourite part of Costa Sol, according to independent reviews.</p>
  <p>This property also has one of the best-rated locations in Costa Sol! Guests are happier about it compared to other properties in the area.</p>
  <p>This property is also rated for the best value in Costa Sol! Guests are getting more for their money when compared to other properties in this city.</p>
</div>

<div class="popular abs">
  <h4>Most popular facilities</h4>
  <ul>
    <li><svg viewBox="0 0 28 22"><path d="M1 16c4-3 7 3 11 0s7 3 11 0 4 0 4 0M1 20c4-3 7 3 11 0s7 3 11 0" stroke="var(--teal)" stroke-width="2" fill="none"/></svg>Swimming pool</li>
    <li><svg viewBox="0 0 28 22"><path d="M3 8a16 16 0 0 1 22 0M7 12a10 10 0 0 1 14 0M11 16a4 4 0 0 1 6 0" stroke="var(--teal)" stroke-width="2" fill="none"/><circle cx="14" cy="19" r="1.6" fill="var(--teal)"/></svg>Free WiFi</li>
    <li><svg viewBox="0 0 28 22"><path d="M4 14l3-7h14l3 7v5H4z" fill="var(--teal)"/><circle cx="9" cy="19" r="2" fill="#fff"/><circle cx="19" cy="19" r="2" fill="#fff"/></svg>Free parking</li>
    <li><svg viewBox="0 0 28 22"><path d="M1 14c4-3 7 3 11 0s7 3 11 0 4 0 4 0M1 19c4-3 7 3 11 0s7 3 11 0" stroke="var(--teal)" stroke-width="2" fill="none"/><path d="M8 2v10M8 2h6" stroke="var(--teal)" stroke-width="2"/></svg>Outdoor pool</li>
    <li><svg viewBox="0 0 28 22"><circle cx="14" cy="11" r="9" stroke="var(--teal)" stroke-width="2" fill="none"/><path d="M7 4l14 14" stroke="var(--teal)" stroke-width="2"/></svg>Non-smoking rooms</li>
    <li><svg viewBox="0 0 28 22"><path d="M4 8l10-6 10 6H4zM7 8v12M21 8v12M4 20h20" stroke="var(--teal)" stroke-width="2" fill="none"/></svg>Terrace</li>
  </ul>
</div>

<div class="surroundings abs">
  <h4>Property surroundings</h4>
  <h5>Closest landmarks</h5>
  <ul>
    <li>Costa Sol Golf Course <span>0.6 km</span></li>
    <li>Dunes Centre <span>1.2 km</span></li>
    <li>City Centre <span>1 km</span></li>
    <li>Aqua Park Costa Sol <span>3.7 km</span></li>
    <li>Costa Sol Lighthouse <span>3.9 km</span></li>
    <li>Playa del Sur <span>4.4 km</span></li>
    <li>Palm Park <span>8.6 km</span></li>
    <li>Hillside Golf Course <span>13.8 km</span></li>
    <li>Playa de Arenas <span>13.9 km</span></li>
    <li>Harbour Point <span>18.5 km</span></li>
  </ul>
  <h5>Restaurants and markets</h5>
  <ul>
    <li>Mercado Sol Express <span>0.6 km</span></li>
    <li>Corner Market Norte <span>0.8 km</span></li>
    <li>Seaside Café <span>1 km</span></li>
    <li>Costa Sol Market <span>1.6 km</span></li>
    <li>Barrio Supermarket <span>3 km</span></li>
    <li>The Olive Tree Restaurant <span>3.4 km</span></li>
    <li>Harbour Grill <span>3.6 km</span></li>
    <li style="color:var(--ink)">Closest airports</li>
    <li>Costa Sol Airport <span>27.8 km</span></li>
  </ul>
</div>

<section class="facilities abs">
  <svg class="abs" style="left:0;top:0" width="1200" height="660" viewBox="0 0 1200 660" preserveAspectRatio="none">
    <defs><linearGradient id="fac" x1="0" x2="0" y1="0" y2="1"><stop offset="0" stop-color="#f5762a"/><stop offset="1" stop-color="#e9492a"/></linearGradient></defs>
    <path d="M0 40 C300 100 500 0 800 50 C1000 80 1100 40 1200 60 V660 H0Z" fill="url(#fac)"/>
  </svg>
  <span class="slide-arrow abs" style="left:105px;top:290px;border:none"><svg width="16" height="30" viewBox="0 0 16 30"><path d="M14 1L2 15l12 14" stroke="#fff" stroke-width="2" fill="none"/></svg></span>
  <span class="slide-arrow abs" style="left:1070px;top:290px;border:none"><svg width="16" height="30" viewBox="0 0 16 30"><path d="M2 1l12 14L2 29" stroke="#fff" stroke-width="2" fill="none"/></svg></span>
  <h2 class="fac-title abs">Facilities of Casa Coral Bungalows</h2>
  <div class="fac-col abs" style="left:173px">
    <svg viewBox="0 0 64 56"><rect x="4" y="6" width="56" height="36" rx="3" stroke="#fff" stroke-width="3" fill="none"/><path d="M24 52h16M32 42v10" stroke="#fff" stroke-width="3"/></svg>
    <h4>Media &amp;<br>Technology</h4>
    <ul><li>Flat-screen TV</li><li>Satellite Channels</li><li>TV</li><li>Laptop safe</li></ul>
  </div>
  <div class="fac-col abs" style="left:350px">
    <svg viewBox="0 0 64 56"><circle cx="14" cy="40" r="11" stroke="#fff" stroke-width="3" fill="none"/><circle cx="50" cy="40" r="11" stroke="#fff" stroke-width="3" fill="none"/><path d="M14 40l12-18h16l8 18M26 22l6 18" stroke="#fff" stroke-width="3" fill="none"/></svg>
    <h4>Activities</h4>
    <ul><li>Water park</li><li>Mini golf</li><li>Diving</li><li>Bowling</li><li>Hiking</li><li>Windsurfing</li><li>Fishing</li><li>Golf course</li><li>Tennis court</li></ul>
  </div>
  <div class="fac-col abs" style="left:527px">
    <svg viewBox="0 0 64 56"><path d="M4 52L32 6l28 46zM32 6v46M22 52l10-18 10 18" stroke="#fff" stroke-width="3" fill="none"/></svg>
    <h4>Outdoors</h4>
    <ul><li>Outdoor furniture</li><li>Outdoor dining area</li><li>Outdoor furniture</li><li>Sun terrace</li><li>Terrace</li><li>Garden</li></ul>
  </div>
  <div class="fac-col abs" style="left:703px">
    <svg viewBox="0 0 64 56"><path d="M8 40a24 24 0 0 1 48 0zM4 44h56M32 10v6" stroke="#fff" stroke-width="3" fill="none"/><circle cx="32" cy="8" r="3" fill="#fff"/></svg>
    <h4>Kitchen</h4>
    <ul><li>Wine glasses</li><li>Child-sized high chair</li><li>Dining table</li><li>Coffee machine</li><li>Stovetop</li><li>Kitchenware</li><li>Electric kettle</li><li>Washing Machine</li><li>Dishwasher</li><li>Microwave</li><li>Refrigerator</li></ul>
  </div>
  <div class="fac-col abs" style="left:877px">
    <svg viewBox="0 0 64 56"><path d="M6 20v30M58 34v16M6 34h52M6 42h52" stroke="#fff" stroke-width="3" fill="none"/><rect x="10" y="24" width="16" height="10" rx="3" stroke="#fff" stroke-width="3" fill="none"/></svg>
    <h4>Room Amenities</h4>
    <ul><li>Iron</li><li>Hypoallergenic pillow</li><li>Non-feather pillow</li><li>Adapter</li><li>Soundproof bed</li><li>Towel rails</li><li>Bedlinen set</li><li>Pool towels</li><li>Plunge pool</li><li>Drying rack for clothing</li><li>Clothes rack</li><li>Tile/Marble floor</li><li>Ironing Facilities</li><li>Safety Deposit Box</li></ul>
  </div>
</section>

<div class="map abs" role="img" aria-label="Street map showing the bungalow location and nearby gardens"></div>

<h2 class="rev-title abs">REVIEWS</h2>
<p class="rev-text abs">Casa Coral Bungalows are located inside a picturesque complex well known for its peaceful and quiet ambient. This single story bungalow is very comfortable and very well equipped with 2 bedrooms, a bathroom with hair dryer and a living/dining room with views to the private garden. The living room has a very comfortable sofa and a flat screen smart TV. The kitchen is fully equipped with a dishwasher, frost free refrigerator, washing machine, microwave, coffee machine, water boiler and cooking utensils. The entire bungalow has Wifi connection, air-conditioning, heating and cleaning service on a weekly basis, all free of charge.</p>
<div class="avatar abs" role="img" aria-label="Guest portrait"></div>
<div class="rev-name abs">Mateo</div>
<div class="rev-lang abs">Languages spoken: English, Spanish</div>

<footer class="footer abs">
  <svg class="abs" style="left:0;top:0" width="1200" height="485" viewBox="0 0 1200 485" preserveAspectRatio="none">
    <path d="M0 40 C250 0 450 80 700 40 C900 10 1050 60 1200 30 V485 H0Z" fill="var(--blue)"/>
    <path d="M0 56 C250 16 450 96 700 56 C900 26 1050 76 1200 46 V485 H0Z" fill="#fff"/>
    <path d="M0 70 C250 30 450 110 700 70 C900 40 1050 90 1200 60 V485 H0Z" fill="var(--blue)"/>
    <path d="M0 90 C250 50 450 130 700 90 C900 60 1050 110 1200 80 V485 H0Z" fill="#fff"/>
    <path d="M0 100 C250 60 450 140 700 100 C900 70 1050 120 1200 90 V485 H0Z" fill="var(--teal)"/>
  </svg>
  <div class="foot-brand abs"><div class="foot-dot"></div><div class="foot-name">CASA CORAL</div></div>
  <div class="foot-col abs" style="left:507px"><h4>Rooms</h4><ul><li>Lorem ipsum dolor</li><li>Consectetur adipiscing</li><li>Fusce eget facilisis</li><li>Donec consequat</li><li>Praesent elementum</li><li>Aliquam posuere</li><li>Aenean a mi cursus</li></ul></div>
  <div class="foot-col abs" style="left:713px"><h4>Locations</h4><ul><li>Lorem ipsum dolor</li><li>Consectetur adipiscing</li><li>Fusce eget facilisis</li><li>Donec consequat</li><li>Praesent elementum</li><li>Aliquam posuere</li><li>Aenean a mi cursus</li></ul></div>
  <div class="foot-col abs" style="left:915px"><h4>Other Links</h4><ul><li>Lorem ipsum dolor</li><li>Consectetur adipiscing</li><li>Fusce eget facilisis</li><li>Donec consequat</li><li>Praesent elementum</li><li>Aliquam posuere</li><li>Aenean a mi cursus</li></ul></div>
  <p class="copyright abs">Copyright 2019 All Rights Reserved</p>
  <div class="social abs"><span style="background:#3b5ea8"></span><span style="background:#2aa3e0"></span><span style="background:#2f6fb6"></span><span style="background:#e0463a"></span></div>
  <span class="lang abs">EN</span>
</footer>

</body>
</html>
```